College Apartment Leasing Flyer

We need a post card/flyer design for a college apartment rental company called RV Stewardship Partners. We lease apartments to college students and would like a post card/flyer that appeal to college students, that are bright colors and eye catching. We would like pictures showcasing our properties with various amenities including big kitchens, living rooms with 50 inch flat screen TVs, large outdoor patios, large rooftop decks, private bathrooms, and much more. Granite countertops, hardwood floors, ceiling fans are some of the many amenities these apartments offer college students.

We want a flyer that advertises these apartments based on the pictures attached, and advertising that we are beginning to kick off our new leasing season. These apartments are ready to be rented, and we are looking to advertise these apartments to Harrowfield College college students looking for apartments.
Updates

Project Deadline Extended
Reason: I would like to see fun design elements incorporated into the flyer. Big, bold print and pictures are the main attraction

Target Market(s)

College students

Industry/Entity Type

Real Estate

Font styles to use
Sans Serif

Colors
abd037
6b449b

Requirements
Must have
• Bright colors, big bold print, pictures of college apartments
Nice to have
• I would like to see multiple pictures with BIG print
Should not have
• Animated pictures

```html
<!DOCTYPE html>
<html lang="en">
<head>
<meta charset="utf-8">
<title>RV Stewardship Partners – For Rent</title>
<link rel="stylesheet" href="https://fonts.googleapis.com/css2?family=Oswald:wght@400;500;700&display=swap">
<style>
  :root{
    --green:#7ed23a;
    --green-edge:#2d6b1a;
    --stripe:#9ee068;
    --purple:#6b449b;
    --black:#000;
    --white:#fff;
    --ink-dark:#1d3a10;
  }
  *{box-sizing:border-box;margin:0;padding:0}
  html,body{width:776px;height:1200px;overflow:hidden;background:var(--black)}
  .flyer{position:relative;width:776px;height:1200px;background:var(--black);font-family:'Oswald',sans-serif;color:var(--white)}
  .block{position:absolute}

  /* header banner */
  .banner{left:57px;top:65px;width:662px;height:194px;background:var(--green);padding:14px 18px 0}
  .banner-photo{position:relative;height:142px;background:linear-gradient(180deg,#7e97ad 0%,#9fb3c2 45%,#5c6e52 75%,#2f3b28 100%)}
  .brand-mark{position:absolute;left:22px;top:12px;font-size:46px;font-weight:500;letter-spacing:2px;color:var(--white)}
  .brand-line{text-align:center;color:var(--ink-dark);font-size:13px;letter-spacing:1px;padding-top:6px}

  /* photo frames */
  .photo-frame{border:12px solid var(--purple);box-shadow:inset 0 0 0 6px var(--black),0 0 18px rgba(107,68,155,.6);padding:6px}
  .photo-frame .photo{width:100%;height:100%}
  .photo-stair{background:linear-gradient(135deg,#d9d2c4 0%,#b9a48a 45%,#8a5a3a 100%)}
  .photo-kitchen{background:linear-gradient(160deg,#e8e2d6 0%,#a46a45 55%,#5a3322 100%)}
  .photo-closet{background:linear-gradient(180deg,#f1ece2 0%,#d8cfbf 60%,#b9a98f 100%)}
  .photo-living{background:linear-gradient(150deg,#f0ebe1 0%,#c49a6c 55%,#7a4a2c 100%)}

  /* amenities word panel */
  .amenities{left:375px;top:298px;width:355px;height:279px;background:var(--green);border:4px solid var(--green-edge);overflow:hidden;text-transform:uppercase;line-height:1}
  .amenity{position:absolute;font-weight:500;white-space:nowrap;line-height:1}
  .vertical{writing-mode:vertical-rl}
  .flipped{transform:rotate(180deg)}
  .amenity-floors{left:10px;top:8px;font-size:26px}
  .amenity-security{left:34px;top:42px;font-size:28px}
  .amenity-system{left:34px;top:74px;font-size:28px}
  .amenity-fans{left:8px;top:44px;font-size:17px}
  .amenity-patio{left:34px;top:114px;font-size:60px;font-weight:700}
  .amenity-laundry{left:36px;top:200px;font-size:18px}
  .amenity-sound{left:198px;top:100px;font-size:18px}
  .amenity-bedrooms{left:230px;top:8px;font-size:20px}
  .amenity-closets{left:253px;top:8px;font-size:20px}
  .amenity-appliances{left:279px;top:120px;font-size:15px}
  .amenity-granite{left:303px;top:8px;font-size:24px}

  /* stripes + tv */
  .stripes{left:569px;top:590px;width:161px;height:160px;background:repeating-linear-gradient(180deg,var(--green) 0 18px,var(--stripe) 18px 22px)}
  .tv{left:569px;top:750px;width:161px;height:125px;background:var(--green);display:flex;align-items:center;justify-content:center;font-size:48px;font-weight:500}

  /* availability */
  .availability{left:31px;top:893px;width:259px;height:285px;background:var(--green);border:3px solid var(--white);text-transform:uppercase}
  .availability .lines{position:absolute;left:14px;top:14px;font-weight:500;line-height:1.3}
  .availability .lines span{display:block}
  .line-now{font-size:24px}
  .line-beds{font-size:34px}
  .line-baths{font-size:24px}
  .line-phone{font-size:26px}
  .line-call{font-size:26px}
  .availability .units{position:absolute;right:10px;top:14px;font-size:40px;line-height:1;font-weight:500;writing-mode:vertical-rl}

  .for-rent{left:298px;top:893px;width:129px;height:285px;background:var(--black);text-align:center;text-transform:uppercase;font-weight:700;font-size:44px;line-height:1.1;padding-top:30px}
  .for-rent .dot{display:block;width:16px;height:16px;border-radius:50%;background:var(--green);margin:18px auto}
</style>
</head>
<body>
<main class="flyer">
  <header class="block banner">
    <div class="banner-photo" role="img" aria-label="City skyline over rooftops and trees">
      <span class="brand-mark">RV</span>
    </div>
    <p class="brand-line">RV Stewardship Partners, LLC</p>
  </header>

  <div class="block photo-frame" style="left:47px;top:298px;width:302px;height:272px">
    <div class="photo photo-stair" role="img" aria-label="Open kitchen with a spiral staircase"></div>
  </div>

  <section class="block amenities" aria-label="Amenities">
    <span class="amenity amenity-floors">Hardwood Floors</span>
    <span class="amenity amenity-security">Security</span>
    <span class="amenity amenity-system">System</span>
    <span class="amenity amenity-fans vertical flipped">Ceiling Fans</span>
    <span class="amenity amenity-patio">Patio</span>
    <span class="amenity amenity-laundry">Washer &amp; Dryer</span>
    <span class="amenity amenity-sound vertical flipped">Surround Sound</span>
    <span class="amenity amenity-bedrooms vertical">Spacious Bedrooms</span>
    <span class="amenity amenity-closets vertical">and Closets</span>
    <span class="amenity amenity-appliances vertical">New Appliances</span>
    <span class="amenity amenity-granite vertical">Granite Counter Tops</span>
  </section>

  <div class="block photo-frame" style="left:47px;top:590px;width:315px;height:285px">
    <div class="photo photo-kitchen" role="img" aria-label="Kitchen with dark cabinets and stainless appliances"></div>
  </div>
  <div class="block photo-frame" style="left:375px;top:590px;width:173px;height:285px">
    <div class="photo photo-closet" role="img" aria-label="Walk-in closet with shelving"></div>
  </div>
  <div class="block stripes" aria-hidden="true"></div>
  <div class="block tv">50" TV</div>

  <section class="block availability">
    <p class="lines">
      <span class="line-now">Now Available</span>
      <span class="line-beds">4 Bedrooms</span>
      <span class="line-baths">3.5 Baths</span>
      <span class="line-phone">555-014-2290</span>
      <span class="line-call">Call Today</span>
    </p>
    <p class="units">Many Units</p>
  </section>

  <div class="block for-rent">For<span class="dot"></span>Rent</div>

  <div class="block photo-frame" style="left:440px;top:893px;width:297px;height:285px">
    <div class="photo photo-living" role="img" aria-label="Living room with ceiling fan, wood floors and flat-screen TV"></div>
  </div>
</main>
</body>
</html>
```